Worldwide Forum on Tension Molecules

We are arranging a meeting in Finland in August: THE 8th WORLDWIDE FORUM ON TENSION MOLECULES IN LIFE AND HEALING - TENSION HANDLING ROUTES AND CIRCUITS.

The program and speakers are included in the Word files. The basic poster arrangement could be a little bit like in the Conference:
http://events.qarvu.net/files/posters/1483956274_17-modulators-ferns.pdf

Basically only the organizers and invited speakers will be listed.

We would like to have some summery maritime background of the kind provided in the stock footage. In addition, we would include some summer views from the City of Turku. We have added a few potential University Campus views in the footage folder.
Updates

Project Deadline Extended
Reason: There was one design that was attractive. We wanted to extend the time available to work along the approach of this design.

Target Market(s)

Scientists in the field of cell stress research

Industry/Entity Type

Management

Requirements
Must have
• There must be the logo of our home university:
• https://www.veltrin.fi/personal/media/3991/vtenglogobasic4c.jpg
• ...somewhere down on the poster, a little bit like QARV in the example above.
• There must also be the logo of the organizing organization Tissue Strain Global Union:
• http://www.tissuestrainreplies.org/?
• All text should be readable (no light text on light background and vice versa)

```html
<!DOCTYPE html>
<html lang="en">
<head>
<meta charset="utf-8">
<title>Worldwide Forum on Tension Molecules</title>
<link href="https://fonts.googleapis.com/css2?family=Lato:ital,wght@0,400;0,700;0,900;1,400;1,700&family=Playfair+Display:ital,wght@1,700&display=swap" rel="stylesheet">
<style>
:root{
  --page:#e8e7e4;
  --ink:#2e2e2e;
  --red:#c8102e;
  --green:#3e8a45;
  --teal:#1f8f86;
  --yellow:#f3d51c;
  --panel-grey:rgba(112,112,112,.9);
  --badge:#8c3a26;
}
*{margin:0;padding:0;box-sizing:border-box}
html,body{width:1200px;height:900px;overflow:hidden;background:var(--page);font-family:"Lato",sans-serif;color:var(--ink)}
.poster{position:absolute;left:295px;top:20px;width:610px;height:860px;overflow:hidden;box-shadow:0 4px 14px rgba(0,0,0,.25)}
.backdrop{position:absolute;inset:0;background:
  linear-gradient(180deg,#c9d3e6 0%,#d6dced 30%,#dfe3ee 45%,transparent 52%),
  linear-gradient(180deg,transparent 48%,#8a7a4e 58%,#c08a33 68%,#6f7a3a 78%,#4d6b2e 88%,#5d6367 92%,#3f4648 100%)}
.uni{position:absolute;left:36px;top:40px;display:flex;align-items:center;gap:12px}
.uni-dot{width:22px;height:22px;border-radius:50%;background:var(--red)}
.uni-name{font-size:18px;font-weight:700;line-height:1.1;color:#222}
.badge{position:absolute;left:390px;top:14px;width:96px;height:96px;border-radius:50%;background:#fff;border:4px solid var(--badge);display:flex;align-items:center;justify-content:center;font-family:"Playfair Display",serif;font-style:italic;font-weight:700;font-size:40px;color:var(--badge)}
.badge sup{font-size:22px}
.title{position:absolute;right:24px;top:122px;text-align:right;font-weight:900;font-size:22px;line-height:28px;color:#3a3a3a;letter-spacing:-.3px}
.theme{position:absolute;right:20px;top:220px;text-align:right;font-weight:900;font-size:27px;line-height:40px;color:#fff;-webkit-text-stroke:1.2px #555;text-shadow:1px 2px 2px rgba(0,0,0,.35);letter-spacing:-.5px}
.details{position:absolute;right:24px;top:302px;text-align:right;font-size:16px;line-height:21px;color:#333}
.details .venue{font-style:italic}
.organizers{position:absolute;left:145px;top:381px;width:221px;height:324px;background:rgba(255,255,255,.93);border-top:6px solid var(--green);padding:12px 9px}
.org-role{font-style:italic;font-weight:900;color:var(--red);font-size:15px;margin-bottom:4px}
.org-entry{padding-left:13px;font-size:12px;font-weight:700;line-height:15px;color:#1e1e1e;margin-bottom:9px}
.speakers{position:absolute;left:375px;top:381px;width:212px;height:427px;background:var(--panel-grey);border-top:6px solid #3a3a3a;padding:6px 6px;color:#fff}
.speakers h2{text-align:center;font-size:14px;font-weight:700;margin-bottom:4px}
.speakers h2 .hl{color:var(--yellow)}
.group{font-size:9.5px;font-style:italic;margin:2px 0 4px}
.group .tag{color:#ff4b5c}
.speakers ol{list-style:none;padding-left:15px;font-size:10px;font-weight:700;line-height:12.2px;margin-bottom:6px}
.speakers .c{color:var(--yellow)}
.gap{height:11px}
.union{position:absolute;left:22px;top:814px;display:flex;align-items:center;gap:8px}
.union-dot{width:32px;height:32px;border-radius:50%;background:var(--teal);border:2px solid #e6f3f1}
.union-name{font-size:16px;font-weight:700;color:#6fe0c8;line-height:1}
.union-note{font-size:6px;color:#c9d2d0;margin-top:2px}
</style>
</head>
<body>
<div class="poster">
  <div class="backdrop" role="img" aria-label="Summer sky over a riverside cathedral tower, autumn trees and a campus building by the water"></div>

  <div class="uni"><span class="uni-dot"></span><div class="uni-name">Veltrin Akademi<br>University</div></div>
  <div class="badge">8<sup>th</sup></div>

  <h1 class="title">WORLDWIDE FORUM ON<br>TENSION MOLECULES IN LIFE<br>AND HEALING</h1>
  <div class="theme">TENSION HANDLING ROUTES<br>AND CIRCUITS</div>
  <div class="details">
    <div><b>August 13-17, 2017</b></div>
    <div class="venue">Harborview Quay Hotel</div>
    <div><b>Turku, Finland</b></div>
  </div>

  <section class="organizers">
    <div class="org-role">ORGANIZER:</div>
    <div class="org-entry">Elina Vaara<br>Veltrin Akademi University<br>Finland</div>
    <div class="org-role">CO-ORGANIZERS:</div>
    <div class="org-entry">Mikael Lindholm<br>Veltrin Akademi University<br>and University of Aurajoki<br>Finland</div>
    <div class="org-entry">Warren Ashby<br>Tissue Strain Global Union<br>(TSGU)<br>University of Eastbrook<br>USA</div>
    <div class="org-entry">Claire Dumont<br>Université Paris Valmont<br>France</div>
  </section>

  <section class="speakers">
    <h2><span class="hl">TSGU Congress</span> 2017</h2>
    <div class="group"><span class="tag">Keynotes</span> (35 min + 10 min):</div>
    <ol>
      <li>1. Maren Voskuil, <span class="c">UK</span></li>
      <li>2. Tove Lindqvist, <span class="c">Denmark</span></li>
      <li>3. Glen Harwick, <span class="c">USA</span></li>
      <li>4. Owen Straub, <span class="c">USA</span></li>
    </ol>
    <div class="group"><span class="tag">Invited speakers</span> (20 min + 10 min):</div>
    <ol>
      <li>1. Luiza Tavares, <span class="c">Brazil</span></li>
      <li>2. Dana Whitlow, <span class="c">USA</span></li>
      <li>3. Miles Carden, <span class="c">USA</span></li>
      <li class="gap"></li>
      <li>5. Avner Tal, <span class="c">Israel</span></li>
      <li>6. Marco Rinaldi, <span class="c">USA</span></li>
      <li>7. Petya Ivanova-Roth, <span class="c">UK</span></li>
      <li>8. Colin R. Mayfield, <span class="c">USA</span></li>
      <li>9. Inès Moreau, <span class="c">France</span></li>
      <li>10. Paula Grenfell, <span class="c">USA</span></li>
      <li>11. Joost Verhaar, <span class="c">The Netherlands</span></li>
      <li>12. Sanna-Maija Korpela, <span class="c">Finland</span></li>
      <li>13. Tobias K. Brandt, <span class="c">Germany</span></li>
      <li>14. Claire Dumont, <span class="c">France</span></li>
      <li>15. Neil B. Ostrow, <span class="c">USA</span></li>
      <li>16. Hiroshi Tamura, <span class="c">Japan</span></li>
      <li>17. Kenji Arima, <span class="c">Japan</span></li>
      <li>18. Roy Fenwick, <span class="c">USA</span></li>
      <li>19. S. Farid Nassar, <span class="c">USA</span></li>
      <li>20. Heikki T. Rantala, <span class="c">Finland</span></li>
      <li>21. Laura Kessling, <span class="c">USA</span></li>
      <li>22. Chiara Benedetti, <span class="c">Italy</span></li>
      <li>23. Daniel Foyle, <span class="c">USA</span></li>
      <li>24. Mark E. Holloway, <span class="c">USA</span></li>
      <li>25. Ruth Ambler, <span class="c">USA</span></li>
    </ol>
  </section>

  <div class="union">
    <span class="union-dot"></span>
    <div><div class="union-name">Tissue Strain Global Union</div><div class="union-note">Home of the tension research journal</div></div>
  </div>
</div>
</body>
</html>
```